New Custom Pizza Box Design Project For Independant Restaurant

We are looking for creative designs for our new custom printed pizza boxes. Designs should include the following:

-Our logo & company name
-A color scheme similar to our current logo
-Our physical and URL addresses & phone number (menu is attached)
-Ability to scale the design across several box sizes (10x10x2, 14x14x2, 18x13x2,
26x18x2)
- Any creative flair you think will make for the best design

Design can be on a white or kraft (tan) box.
Designs can be either two or three ink colors.

***Please note, designs must be able to be screen printed on boxes***
Updates

Reason: Still debating which to choose

Target Market(s)

Industry/Entity Type

Pizza Delivery

Font styles to use
Other font styles liked:
• Please use font similar to our logo text

Requirements
Must have
• -2 or 3 ink colors
• -company name, address, phone number, URL
• -company logo and colors
• -flexibility to use on different box sizes (10x10x2, 14x14x2, 18x13x2,
• 26x18x2)
• -utilize full printable area on boxes (including 2" dimension on box sides)
• ***Please note, designs must be able to be screen printed on boxes***
Should not have
• Design features with strong similarities to existing designs of other pizzerias

```html
<!DOCTYPE html>
<html lang="en">
<head>
<meta charset="utf-8">
<title>Marco's Hilltop Pizzeria – Pizza Box Dieline</title>
<link href="https://fonts.googleapis.com/css2?family=Zilla+Slab:wght@500;700&display=swap" rel="stylesheet">
<style>
  :root{
    --paper:#ffffff;
    --stage:#f3f3f3;
    --yellow:#f2b51e;
    --brown:#6b3a1f;
    --cut:#e2372b;
    --art-light:#fbf6ea;
    --art-mid:#f3e6c8;
  }
  html,body{margin:0;padding:0;width:1200px;height:1156px;overflow:hidden;background:var(--stage);}
  .dieline{position:absolute;left:311px;top:8px;width:577px;height:1140px;display:block;}
  .slab{font-family:"Zilla Slab",Georgia,serif;}
  .brand{font-family:"Zilla Slab",Georgia,serif;font-weight:700;fill:var(--brown);text-anchor:middle;letter-spacing:1px;}
  .phone{font-family:"Zilla Slab",Georgia,serif;font-weight:500;fill:var(--brown);text-anchor:middle;}
  .url{font-family:"Zilla Slab",Georgia,serif;font-weight:700;fill:var(--yellow);text-anchor:middle;}
  .url-dark{fill:var(--brown);}
  .address{font-family:"Zilla Slab",Georgia,serif;font-weight:500;fill:var(--brown);text-anchor:middle;}
  .badge-shape{fill:var(--yellow);}
  .badge-text{font-family:"Zilla Slab",Georgia,serif;font-weight:700;fill:var(--brown);text-anchor:middle;}
  .badge-text-light{fill:var(--paper);}
  .label{font-family:"Zilla Slab",Georgia,serif;font-weight:500;fill:var(--brown);text-anchor:middle;}
  .cut-line{fill:none;stroke:var(--cut);stroke-width:3;stroke-linejoin:miter;}
  .panel{fill:var(--paper);}
  .band{fill:var(--yellow);}
</style>
</head>
<body>
<svg class="dieline" viewBox="790 8 675 1334" xmlns="http://www.w3.org/2000/svg">
  <defs>
    <linearGradient id="art-tone" x1="0" y1="0" x2="1" y2="1">
      <stop offset="0" stop-color="var(--art-light)"/>
      <stop offset="1" stop-color="var(--art-mid)"/>
    </linearGradient>
    <polygon id="starburst" points="1,0 0.773,0.207 0.866,0.5 0.566,0.566 0.5,0.866 0.207,0.773 0,1 -0.207,0.773 -0.5,0.866 -0.566,0.566 -0.866,0.5 -0.773,0.207 -1,0 -0.773,-0.207 -0.866,-0.5 -0.566,-0.566 -0.5,-0.866 -0.207,-0.773 0,-1 0.207,-0.773 0.5,-0.866 0.566,-0.566 0.866,-0.5 0.773,-0.207"/>
    <g id="slice-chart">
      <circle r="22" fill="var(--paper)" stroke="var(--brown)" stroke-width="2"/>
      <circle r="10.5" fill="none" stroke="var(--brown)" stroke-width="21" stroke-dasharray="8.25 8.25"/>
    </g>
    <g id="wall-content">
      <use href="#starburst" class="badge-shape" transform="translate(-160 0) scale(60 38)"/>
      <text class="badge-text" x="-160" y="-4" font-size="17">ORDER</text>
      <text class="badge-text" x="-160" y="16" font-size="17">ONLINE</text>
      <text class="phone" x="0" y="-4" font-size="38">555-0148</text>
      <text class="address" x="0" y="14" font-size="8">1742 Alder Street Eastfield Plaza</text>
      <text class="url" x="0" y="34" font-size="17">marcoshilltop.com</text>
      <text class="brand" x="172" y="-16" font-size="10">MARCO'S</text>
      <text class="brand" x="172" y="0" font-size="13">HILLTOP</text>
      <text class="brand" x="172" y="16" font-size="10">PIZZERIA</text>
    </g>
  </defs>

  <!-- panels -->
  <rect class="panel" x="800" y="15" width="655" height="1225"/>
  <rect class="panel" x="893" y="1240" width="467" height="95"/>

  <!-- lid -->
  <g class="lid">
    <text class="brand" x="1128" y="548" font-size="14">MARCO'S</text>
    <text class="brand" x="1128" y="574" font-size="22">HILLTOP</text>
    <text class="brand" x="1128" y="598" font-size="14">PIZZERIA</text>
    <text class="phone" x="1128" y="638" font-size="20">555-0148</text>
    <text class="address" x="1128" y="649" font-size="5">1742 Alder Street Eastfield Plaza</text>
    <text class="url" x="1128" y="660" font-size="10">marcoshilltop.com</text>
  </g>

  <!-- lid front strip (printed upside down) -->
  <g class="lid-front" transform="rotate(180 1126 729) translate(1126 736)">
    <use href="#wall-content"/>
  </g>

  <!-- box floor -->
  <g class="floor">
    <rect x="895" y="777" width="463" height="461" fill="url(#art-tone)" role="img" aria-label="Hand-drawn pizza with scattered vegetables and herbs in brown and yellow line art"/>
    <rect class="band" x="1053" y="777" width="147" height="461" opacity="0.92"/>
    <text class="phone" x="1126" y="815" font-size="29">555-0148</text>
    <circle cx="1126" cy="1008" r="72" fill="var(--paper)" stroke="var(--yellow)" stroke-width="3"/>
    <text class="brand" x="1126" y="990" font-size="15">MARCO'S</text>
    <text class="brand" x="1126" y="1016" font-size="22">HILLTOP</text>
    <text class="brand" x="1126" y="1040" font-size="15">PIZZERIA</text>
    <use href="#starburst" fill="var(--paper)" transform="translate(1130 1200) scale(28 18)"/>
    <text class="badge-text" x="1130" y="1198" font-size="9">ORDER</text>
    <text class="badge-text" x="1130" y="1208" font-size="9">ONLINE</text>
    <text class="url url-dark" x="1126" y="1231" font-size="15">marcoshilltop.com</text>
    <text class="label" x="1306" y="1157" font-size="11">for 3 people</text>
    <use href="#slice-chart" transform="translate(1306 1182)"/>
    <text class="label" x="1306" y="1224" font-size="11">8 pcs</text>
  </g>

  <!-- left wall -->
  <rect class="band" x="800" y="777" width="93" height="463"/>
  <g class="side-wall" transform="translate(846 1008) rotate(90)">
    <text class="phone" x="30" y="-4" font-size="48">555-0148</text>
    <text class="url url-dark" x="30" y="32" font-size="22">marcoshilltop.com</text>
    <text class="brand" x="-190" y="-14" font-size="9">MARCO'S</text>
    <text class="brand" x="-190" y="2" font-size="13">HILLTOP</text>
    <text class="brand" x="-190" y="16" font-size="9">PIZZERIA</text>
    <use href="#slice-chart" transform="translate(190 0) rotate(-90)"/>
    <text class="label" x="190" y="-28" font-size="10">for 3 people</text>
    <text class="label" x="190" y="36" font-size="10">8 pcs</text>
  </g>

  <!-- right wall -->
  <rect class="band" x="1360" y="777" width="95" height="463"/>
  <g class="side-wall" transform="translate(1407 1008) rotate(-90)">
    <text class="phone" x="-30" y="-4" font-size="48">555-0148</text>
    <text class="url url-dark" x="-30" y="32" font-size="22">marcoshilltop.com</text>
    <text class="brand" x="-190" y="-14" font-size="9">MARCO'S</text>
    <text class="brand" x="-190" y="2" font-size="13">HILLTOP</text>
    <text class="brand" x="-190" y="16" font-size="9">PIZZERIA</text>
    <use href="#slice-chart" transform="translate(190 0) rotate(90)"/>
    <text class="label" x="190" y="-28" font-size="10">for 3 people</text>
    <text class="label" x="190" y="36" font-size="10">8 pcs</text>
  </g>

  <!-- front wall -->
  <g class="front-wall" transform="translate(1126 1290)">
    <use href="#wall-content"/>
  </g>

  <!-- cut and fold lines -->
  <g class="cut-line">
    <path d="M800,1240 V15 H880 L893,108"/>
    <path d="M893,15 H1360"/>
    <path d="M1360,108 L1375,15 H1455 V1240 H1360 V1335 H893 V1240 H800"/>
    <path d="M893,15 V215 M1360,15 V215"/>
    <path d="M893,108 H1360 M893,125 H1360"/>
    <path d="M800,215 H1455 M800,683 H1455 M800,775 H1455"/>
    <path d="M893,215 V1240 M1360,215 V1240 M893,1240 H1360"/>
  </g>
</svg>
</body>
</html>
```